Bright Oak Fitness Facility Business Cards

Business Card Design that incorporates the logo and tagline

Target Market(s)

Fitness, People Who Exercise

Contact Information for Business Card

2817 Mossgrove Bend Road
Harlow Springs, Ohio 43190
Phone: 614-555-Jump (5867)
www.brightoakfitness.example
info@brightoakfitness.example

Requirements
Must have
• Logo, Address, Website, email and tagline "Stronger Every Day". Colors should be red/black/grey/white

```html
<!DOCTYPE html>
<html lang="en">
<head>
<meta charset="utf-8">
<title>Bright Oak Fitness – Business Cards</title>
<link rel="stylesheet" href="https://fonts.googleapis.com/css2?family=Poppins:wght@400;500;600&display=swap">
<style>
  :root {
    --backdrop: #4a4c50;
    --card-dark: #1e1e20;
    --card-light: #ffffff;
    --brand-red: #e3222b;
    --ink: #2b2b2d;
    --grey: #8c8c90;
    --silver: #b9b9bd;
    --divider: #9a9a9e;
  }
  * { box-sizing: border-box; margin: 0; padding: 0; }
  html, body { width: 1200px; height: 880px; overflow: hidden; }
  body {
    background: var(--backdrop);
    font-family: "Poppins", sans-serif;
    display: flex;
    flex-direction: column;
    align-items: center;
    justify-content: center;
    gap: 56px;
  }
  .card {
    width: 580px;
    height: 332px;
    border-radius: 22px;
    position: relative;
    overflow: hidden;
  }

  /* Back of card */
  .card-back {
    background: var(--card-dark);
    display: flex;
    flex-direction: column;
    align-items: center;
    justify-content: center;
    gap: 22px;
  }
  .brand-lockup { display: flex; align-items: center; gap: 12px; white-space: nowrap; }
  .brand-dot { width: 18px; height: 18px; border-radius: 50%; flex: none; }
  .card-back .brand-dot { background: var(--silver); }
  .card-back .brand-name {
    font-weight: 600;
    font-size: 34px;
    color: var(--silver);
    letter-spacing: 1px;
  }
  .tagline {
    font-size: 14px;
    font-weight: 500;
    letter-spacing: 9px;
    color: var(--grey);
  }

  /* Front of card */
  .card-front {
    background: var(--card-light);
    display: flex;
    align-items: center;
    padding: 0 30px 0 34px;
  }
  .front-brand { width: 240px; display: flex; justify-content: center; }
  .card-front .brand-dot { background: var(--brand-red); width: 14px; height: 14px; }
  .card-front .brand-name {
    font-weight: 600;
    font-size: 21px;
    color: var(--brand-red);
  }
  .front-divider {
    width: 1px;
    height: 190px;
    background: var(--divider);
    margin: 0 24px 0 18px;
    flex: none;
  }
  .contact { color: var(--ink); font-size: 13px; line-height: 1.45; white-space: nowrap; }
  .person-name {
    font-size: 22px;
    font-weight: 600;
    color: var(--brand-red);
    line-height: 1.1;
  }
  .person-role { font-size: 14px; margin-bottom: 12px; }
  .address { margin-bottom: 12px; font-size: 14px; }
  .contact-line { display: flex; align-items: center; gap: 9px; }
  .contact-line svg { width: 12px; height: 12px; flex: none; fill: var(--brand-red); }
</style>
</head>
<body>

  <section class="card card-back" aria-label="Card back">
    <div class="brand-lockup">
      <span class="brand-dot"></span>
      <span class="brand-name">Bright Oak Fitness</span>
    </div>
    <p class="tagline">Stronger Every Day</p>
  </section>

  <section class="card card-front" aria-label="Card front">
    <div class="front-brand">
      <div class="brand-lockup">
        <span class="brand-dot"></span>
        <span class="brand-name">Bright Oak Fitness</span>
      </div>
    </div>
    <div class="front-divider"></div>
    <div class="contact">
      <p class="person-name">DANA REYES</p>
      <p class="person-role">Founder &amp; CEO</p>
      <p class="address">2817 Mossgrove Bend Road<br>Harlow Springs, Ohio 43190</p>
      <p class="contact-line">
        <svg viewBox="0 0 24 24" aria-hidden="true"><path d="M6.6 10.8a15 15 0 0 0 6.6 6.6l2.2-2.2a1 1 0 0 1 1-.25 11.4 11.4 0 0 0 3.6.57 1 1 0 0 1 1 1V20a1 1 0 0 1-1 1A17 17 0 0 1 3 4a1 1 0 0 1 1-1h3.5a1 1 0 0 1 1 1c0 1.25.2 2.45.57 3.57a1 1 0 0 1-.25 1z"/></svg>
        614-555-Jump (5867)
      </p>
      <p class="contact-line">
        <svg viewBox="0 0 24 24" aria-hidden="true"><path d="M2 5h20v14H2z M2 5l10 8 10-8"/></svg>
        info@brightoakfitness.example
      </p>
      <p class="contact-line">
        <svg viewBox="0 0 24 24" aria-hidden="true"><circle cx="12" cy="12" r="10"/></svg>
        www.brightoakfitness.example
      </p>
    </div>
  </section>

</body>
</html>
```